IT-Dienstleister für Projektmanagementsoftware sucht Broschüre im DIN-A4-Format
Zielgruppe
Wir sind ein IT-Dienstleister für Projektmanagementsoftware. Wir installieren, migrieren und entwickeln Software für das Projektmanagement auf Basis von Veltrano Technologien. Unsere Zielgruppe sind mittelständische Unternehmen und große Konzerne. Je komplexer das Projektmanagement in einem Unternehmen, desto eher helfen unsere Lösungen.
Aufgabenstellung
Es soll eine DIN A4 Hochglanz Broschüre für eine Messe entstehen. Wir haben bereits ein Grobkonzept mit Bildauswahl und Texten erstellt. An diesem soll sich orientiert werden. Bezüglich desDesigns, der Anordnung der Texte und Bilder etc. besteht völlige Freiheit. Weitere Orientierung bieten unsere Webseiten haldewiegand.de und quilbyte.de. Die Texte und Screenshots sind teilweise nur Platzhalter und müssen später noch angepasst werden können. Wir benötigen daher unbedingt die Rohdaten des Designs.

```html
<!DOCTYPE html>
<html lang="de">
<head>
<meta charset="utf-8">
<title>Halde &amp; Wiegand – Broschüre</title>
<link rel="stylesheet" href="https://fonts.googleapis.com/css2?family=Roboto:wght@300;400;500&display=swap">
<style>
  :root{
    --stage:#dcdde1;
    --divider:#ffffff;
    --paper:#f2f2f2;
    --green:#8dc63f;
    --navy:#0f3358;
    --ink:#4a4a4a;
    --white:#ffffff;
  }
  *{box-sizing:border-box;margin:0;padding:0}
  html,body{width:1200px;height:3750px;overflow:hidden;background:var(--divider);font-family:"Roboto",Arial,sans-serif}
  .sheet{display:flex;flex-direction:column;gap:12px;width:1200px;height:3750px}
  .stage{background:var(--stage);display:flex;align-items:center;justify-content:center}
  .stage--cover{height:930px}
  .stage--spread{height:930px}
  .stage--back{height:930px}
  .stage--inner{height:924px}
  .spread{display:flex;box-shadow:0 10px 30px rgba(0,0,0,.18)}
  .page{position:relative;overflow:hidden;background:var(--paper)}
  .stage > .page{box-shadow:0 10px 30px rgba(0,0,0,.18)}
  .page--cover-lg{width:540px;height:764px;font-size:24px}
  .page--spread{width:470px;height:665px;font-size:21px}
  .page--back-lg{width:580px;height:820px;font-size:26px}
  .page--inner{width:530px;height:750px;font-size:24px}

  /* cover */
  .brand{position:absolute;top:7%;right:8%;font-weight:400;font-size:.95em;color:var(--ink);letter-spacing:.01em;display:flex;align-items:center;gap:.4em}
  .brand__dot{width:.35em;height:.35em;background:var(--green)}
  .earth-photo{position:absolute;inset:0;
    background:
      radial-gradient(ellipse at 85% 20%, #5e6f80 0 8%, transparent 20%),
      radial-gradient(ellipse at 40% 55%, #6f8fb3 0%, #3e628c 40%, #1d3d66 80%);
    clip-path:polygon(0 38%,100% 27%,100% 100%,0 100%)}
  .cover-title{position:absolute;left:10%;top:64%;font-weight:300;font-size:1.05em;line-height:1.3;color:var(--white)}
  .cover-title__accent{color:var(--green)}

  /* back */
  .back-photo{position:absolute;inset:0;
    background:radial-gradient(ellipse at 80% 45%, #2d5580 0%, #173e69 45%, var(--navy) 85%);
    clip-path:polygon(0 37%,100% 29%,100% 100%,0 100%)}
  .back-quote{position:absolute;left:10%;top:15%;width:80%;font-size:.52em;line-height:1.45;color:var(--green)}
  .contact{position:absolute;left:10%;top:68%;font-size:.33em;line-height:1.7;color:var(--white)}
  .contact__block{margin-bottom:1.3em}
  .contact__row{display:flex;align-items:center;gap:.4em}
  .contact__row svg{width:1em;height:1em;fill:var(--white)}
  .contact__web{margin-top:1.3em;color:var(--green);font-weight:500}

  /* inner spread */
  .launch-photo{position:absolute;inset:0;
    background:
      radial-gradient(ellipse at 45% 68%, #f3c27a 0%, #d98a3a 10%, transparent 28%),
      radial-gradient(ellipse at 25% 85%, #f4f4f4 0%, #d9dde2 25%, transparent 45%),
      linear-gradient(180deg,#2f5e9e 0%,#6e9bd0 45%,#b9d0e8 100%)}
  .inner-sky{position:absolute;inset:0;background:linear-gradient(160deg,#2d5ea6 0%,#4f80c4 55%,#89aede 100%);clip-path:polygon(0 0,56% 0,0 86%)}
  .invite{position:absolute;left:26%;top:56%;width:62%;font-weight:400;font-size:1.05em;line-height:1.2;color:var(--ink)}
  .invite__accent{color:var(--green)}
  .portraits{position:absolute;left:17%;top:79%;display:flex;gap:.55em}
  .portrait{width:2em;height:2em;border-radius:50%;background:radial-gradient(circle at 40% 40%,#b8925f,#6a4a2c)}
  .partner{position:absolute;bottom:6%;left:10%;font-size:.75em;color:var(--ink);display:flex;align-items:center;gap:.35em}
  .partner__dot{width:.7em;height:.7em;border-radius:50%;background:var(--ink)}
  .brand--foot{top:auto;bottom:6%;right:8%;font-size:.75em}
</style>
</head>
<body>
<main class="sheet">

  <section class="stage stage--cover">
    <article class="page page--cover-lg">
      <div class="earth-photo" role="img" aria-label="Erde aus dem Orbit mit Raumstation"></div>
      <div class="brand"><span>Halde &amp; Wiegand</span><span class="brand__dot"></span></div>
      <h1 class="cover-title"><span class="cover-title__accent">Softwarelösungen</span> für<br>digitale Unternehmens-<br>prozesse</h1>
    </article>
  </section>

  <section class="stage stage--spread">
    <div class="spread">
      <article class="page page--spread">
        <div class="back-photo" role="img" aria-label="Erdoberfläche mit Wolken in Dunkelblau"></div>
        <p class="back-quote">»Ihilique sumquasped mo in nonsequi consenducit adisimil ipidebi scimus ullaccusa et quas voluptatur, nonsequiam quodipi cidenie ntiatur. Qui autem qui.«</p>
        <div class="contact">
          <div class="contact__block">Halde &amp; Wiegand GmbH<br>Lindenhof-Ring 14<br>80331 München</div>
          <div class="contact__row"><svg viewBox="0 0 24 24"><path d="M6.6 10.8a15 15 0 006.6 6.6l2.2-2.2c.3-.3.7-.4 1-.2 1.1.4 2.3.6 3.6.6.6 0 1 .4 1 1V20c0 .6-.4 1-1 1A17 17 0 013 4c0-.6.4-1 1-1h3.5c.6 0 1 .4 1 1 0 1.3.2 2.5.6 3.6.1.3 0 .7-.2 1z"/></svg>+49 89 555 01 20-0</div>
          <div class="contact__row"><svg viewBox="0 0 24 24"><path d="M6 3h12v5H6zM4 9h16a2 2 0 012 2v6h-4v4H6v-4H2v-6a2 2 0 012-2zm4 7v3h8v-3z"/></svg>+49 89 555 01 20-999</div>
          <div class="contact__row"><svg viewBox="0 0 24 24"><path d="M2 5h20v14H2zm2 2v.5l8 5 8-5V7z"/></svg>service@haldewiegand.de</div>
          <div class="contact__web">www.haldewiegand.de</div>
        </div>
      </article>
      <article class="page page--spread">
        <div class="earth-photo" role="img" aria-label="Erde aus dem Orbit mit Raumstation"></div>
        <div class="brand"><span>Halde &amp; Wiegand</span><span class="brand__dot"></span></div>
        <h1 class="cover-title"><span class="cover-title__accent">Softwarelösungen</span> für<br>digitale Unternehmens-<br>prozesse</h1>
      </article>
    </div>
  </section>

  <section class="stage stage--back">
    <article class="page page--back-lg">
      <div class="back-photo" role="img" aria-label="Erdoberfläche mit Wolken in Dunkelblau"></div>
      <p class="back-quote">»Ihilique sumquasped mo in nonsequi consenducit adisimil ipidebi scimus ullaccusa et quas voluptatur, nonsequiam quodipi cidenie ntiatur. Qui autem qui.«</p>
      <div class="contact">
        <div class="contact__block">Halde &amp; Wiegand GmbH<br>Lindenhof-Ring 14<br>80331 München</div>
        <div class="contact__row"><svg viewBox="0 0 24 24"><path d="M6.6 10.8a15 15 0 006.6 6.6l2.2-2.2c.3-.3.7-.4 1-.2 1.1.4 2.3.6 3.6.6.6 0 1 .4 1 1V20c0 .6-.4 1-1 1A17 17 0 013 4c0-.6.4-1 1-1h3.5c.6 0 1 .4 1 1 0 1.3.2 2.5.6 3.6.1.3 0 .7-.2 1z"/></svg>+49 89 555 01 20-0</div>
        <div class="contact__row"><svg viewBox="0 0 24 24"><path d="M6 3h12v5H6zM4 9h16a2 2 0 012 2v6h-4v4H6v-4H2v-6a2 2 0 012-2zm4 7v3h8v-3z"/></svg>+49 89 555 01 20-999</div>
        <div class="contact__row"><svg viewBox="0 0 24 24"><path d="M2 5h20v14H2zm2 2v.5l8 5 8-5V7z"/></svg>service@haldewiegand.de</div>
        <div class="contact__web">www.haldewiegand.de</div>
      </div>
    </article>
  </section>

  <section class="stage stage--inner">
    <div class="spread">
      <article class="page page--inner">
        <div class="launch-photo" role="img" aria-label="Raumfähre beim Start von der Startrampe mit Rauchwolken"></div>
      </article>
      <article class="page page--inner">
        <div class="inner-sky" role="img" aria-label="Blauer Himmel als Fortsetzung des Startbilds"></div>
        <h2 class="invite">Kommen Sie mit auf unsere digitale Arche Noah in die Zukunft des <span class="invite__accent">Projektmanagements!</span></h2>
        <div class="portraits">
          <div class="portrait" role="img" aria-label="Tierfoto im Kreis"></div>
          <div class="portrait" role="img" aria-label="Tierfoto im Kreis"></div>
          <div class="portrait" role="img" aria-label="Tierfoto im Kreis"></div>
          <div class="portrait" role="img" aria-label="Tierfoto im Kreis"></div>
          <div class="portrait" role="img" aria-label="Tierfoto im Kreis"></div>
        </div>
        <div class="partner"><span class="partner__dot"></span><span>Quilbyte</span></div>
        <div class="brand brand--foot"><span>Halde &amp; Wiegand</span><span class="brand__dot"></span></div>
      </article>
    </div>
  </section>

</main>
</body>
</html>
```